Company's Core Values to be on our Office Walls

We are a biotechnology consulting company in Massachusetts with about 40 employees. Please check out velmora.com for our look and more information on our business.

We have 4 core values in the company which we would like to display in our office. (Could be on our walls, could be placed in our website, could be placed anywhere. - We would like a multi-use for this graphic but PRIMARILY on our walls.)
No measurements involved yet, hence we'd like the source file to enable us to stretch the graphics. What's important is to see the designs in this contest.

Design: Looking for a wall display - decal, glass board, vinyl (we're open)
- of our Core Values to have in our reception. We want a Double-Helix
incorporated as the core values are "in our DNA" like the one attached
(would like to see some designs with the exact photo and some used as
inspiration for a unique creative design). Open to various sizes, we have a
few different walls we could place them on.

We are looking for a creative Core Value display to have in our new office. We want a sleek, out of the box design!

Velmora's 4 Core Values are:
> Put Others First
> Have the Courage to Take Action
> Take Personal Responsibility
> Have fun!
***We welcome any infographics per core value. We are open to your creativity!

**WE WANT THE ACTUAL CORE VALUES ON DISPLAY**
We already have a brand (attached).
Need our actual values on display in office.
We want the actual values on the wall, our logo can be incorporated but not
necessarily.

Overview of company: Young consulting firm for biotech and pharmaceuticals
in the Greater Boston area. We are service based, our employees are
engineers and specialists that work on our clients site. Company was
established in 2010, we moved into our New England office 3 months ago!

Colors: Our main color is blue but we also use orange, green, purple, and
teal. See velmora.com for our colors.

Target Market(s)

New Hires and Clients - We want to impress them!
Employees and clients - we want employees inspired by the core
values and clients to be impressed by them/separate us from the competition.

Industry/Entity Type

Biotechnology

Font styles to use
Sans Serif

Colors

Designer to choose colors to be used in the design.

Requirements
Must have
• Creativity!
• Some sort of tie to science/biotech
• Color - Blue is our company color but would like others as well. See website for brand colors.

```html
<!DOCTYPE html>
<html lang="en">
<head>
<meta charset="utf-8">
<title>Velmora Group — Core Values</title>
<link href="https://fonts.googleapis.com/css2?family=Montserrat:wght@600;700&display=swap" rel="stylesheet">
<style>
  :root {
    --page-bg: #d9d9d9;
    --navy-deep: #0c2240;
    --navy: #143a66;
    --blue-mid: #21578f;
    --helix-light: #a9cdee;
    --helix-mid: #5b93cc;
    --helix-deep: #2a5f97;
    --bar-tint: rgba(110, 170, 215, 0.6);
    --white: #ffffff;
    --brand-ink: #14365a;
  }
  * { margin: 0; padding: 0; box-sizing: border-box; }
  html, body {
    width: 1200px; height: 1200px; overflow: hidden;
    background: var(--page-bg);
    font-family: "Montserrat", sans-serif;
  }
  .poster {
    position: absolute; left: 244px; top: 50px;
    width: 711px; height: 1100px; overflow: hidden;
    background: linear-gradient(165deg, var(--blue-mid) 0%, var(--navy) 50%, var(--navy-deep) 100%);
  }
  .helix-visual {
    position: absolute; left: 0; top: 0; width: 711px; height: 690px;
    background:
      radial-gradient(ellipse 30% 42% at 28% 22%, var(--helix-light), transparent 72%),
      radial-gradient(ellipse 26% 36% at 60% 40%, rgba(169,205,238,0.85), transparent 72%),
      radial-gradient(ellipse 22% 30% at 78% 70%, rgba(91,147,204,0.8), transparent 72%),
      linear-gradient(150deg, var(--helix-mid) 0%, var(--helix-deep) 55%, rgba(42,95,151,0) 100%);
    -webkit-mask-image: linear-gradient(180deg, #000 70%, transparent 100%);
            mask-image: linear-gradient(180deg, #000 70%, transparent 100%);
  }
  .title { font-weight: 700; }
  .title-line {
    position: absolute; color: var(--white);
    font-size: 96px; line-height: 1; white-space: nowrap;
  }
  .title-core { left: 32px; top: 413px; }
  .title-values { left: 58px; top: 507px; }
  .value-bar {
    position: absolute; height: 46px; display: flex; align-items: center;
    color: var(--white); font-weight: 600; font-size: 27px; white-space: nowrap;
    background: linear-gradient(90deg, transparent 0%, var(--bar-tint) 12%, rgba(70,130,190,0.35) 70%, transparent 100%);
    box-shadow: 0 8px 10px -6px rgba(0,0,0,0.45);
  }
  .value-1 { left: 38px;  top: 608px; width: 357px; padding-left: 39px; }
  .value-2 { left: 80px;  top: 677px; width: 538px; padding-left: 28px; }
  .value-3 { left: 159px; top: 748px; width: 485px; padding-left: 33px; }
  .value-4 { left: 395px; top: 818px; width: 263px; padding-left: 41px; }
  .brand-corner { position: absolute; left: 0; top: 0; }
  .brand-name {
    position: absolute; left: 408px; width: 260px; top: 1028px; text-align: center;
    color: var(--brand-ink); font-weight: 600; font-size: 26px; letter-spacing: 2px;
    white-space: nowrap;
  }
</style>
</head>
<body>
  <main class="poster">
    <div class="helix-visual" role="img" aria-label="Blue double helix DNA strand rendering"></div>

    <h1 class="title">
      <span class="title-line title-core">CORE</span>
      <span class="title-line title-values">VALUES</span>
    </h1>

    <div class="value-bar value-1">Put Others First</div>
    <div class="value-bar value-2">Have the Courage to Take Action</div>
    <div class="value-bar value-3">Take Personal Responsibility</div>
    <div class="value-bar value-4">Have fun!</div>

    <svg class="brand-corner" width="711" height="1100" viewBox="0 0 711 1100" aria-hidden="true">
      <path d="M329 1100 C 420 980, 560 915, 711 897 L711 1100 Z" fill="var(--white)"/>
      <circle cx="538" cy="958" r="52" fill="var(--brand-ink)"/>
    </svg>
    <div class="brand-name">VELMORA GROUP</div>
  </main>
</body>
</html>
```